Brightwell Consulting Business Card Design

Business Card Design for Brightwell Consulting. Brightwell Consulting is a boutique consultancy based in Riverton, OH., that specializes in marketing strategy, organization planning, and leadership development. We provide solutions for small businesses and startups as well as Summit 400 companies.

http://brightwellconsulting.example/

Target Market(s)

We provide solutions for small businesses and startups as well as Summit 400 companies.

Industry/Entity Type

Consulting

Contact Information for Business Card

Two sided business card with priority on contact information, logo, tag line (Momentum to Plan More, Lead More, Grow More)

Colors

Designer to choose colors to be used in the design.

Requirements
Must have
• contact information, logo, tag line (Momentum to Plan More, Lead More, Grow More)
• Simple no over communication.
Nice to have
• I would like to see different placements of logo and creative use of both sides of the card
Should not have
• Do not put too much information on the card.

```html
<!DOCTYPE html>
<html lang="en">
<head>
<meta charset="utf-8">
<title>Brightwell Consulting Business Card</title>
<link href="https://fonts.googleapis.com/css2?family=Open+Sans:wght@400;600;700&display=swap" rel="stylesheet">
<style>
  :root {
    --ink: #0b0b0b;
    --paper: #ffffff;
    --backdrop: #e8ebeb;
    --rule: #2a2a2a;
    --muted: #1c1c1c;
  }
  * { box-sizing: border-box; margin: 0; padding: 0; }
  html, body {
    width: 1200px; height: 1024px; overflow: hidden;
    background: var(--backdrop);
    font-family: "Open Sans", Arial, sans-serif;
  }
  .sheet {
    position: relative; width: 1200px; height: 1024px;
    display: flex; flex-direction: column; align-items: center; justify-content: center; gap: 64px;
  }
  .card {
    position: relative; width: 620px; height: 354px; overflow: hidden;
    box-shadow: 0 10px 26px rgba(0,0,0,.16);
  }
  /* Front */
  .card-front { background: var(--ink); }
  .card-front .pattern-area {
    position: absolute; inset: 0;
    background: radial-gradient(circle at 50% 50%, #161616 0%, #0b0b0b 75%);
  }
  .wordmark {
    display: flex; align-items: flex-start; gap: 12px;
    font-weight: 700; letter-spacing: .5px; line-height: 1.1;
    white-space: nowrap;
  }
  .wordmark .mark-dot { width: 14px; height: 14px; border-radius: 50%; flex: none; margin-top: .38em; }
  .wordmark .mark-name { display: block; }
  .card-front .wordmark {
    position: absolute; left: 50%; top: 50%; transform: translate(-50%, -50%);
    color: var(--paper); font-size: 40px;
  }
  .card-front .mark-dot { background: var(--paper); }
  /* Back */
  .card-back { background: var(--paper); color: var(--ink); }
  .card-back .wordmark {
    position: absolute; left: 34px; top: 122px;
    font-size: 25px;
  }
  .card-back .mark-dot { background: var(--ink); width: 12px; height: 12px; margin-top: .4em; }
  .divider {
    position: absolute; left: 270px; top: 46px; width: 1px; height: 214px; background: var(--rule);
  }
  .contact { position: absolute; left: 292px; top: 46px; font-size: 14px; line-height: 1.45; color: var(--muted); white-space: nowrap; }
  .contact .name { font-size: 19px; font-weight: 700; color: var(--ink); line-height: 1.2; }
  .contact .role { margin-bottom: 12px; }
  .contact .company { margin-bottom: 12px; }
  .contact .line { display: flex; align-items: center; gap: 10px; margin-bottom: 7px; }
  .contact svg { flex: none; }
  .tagline-band {
    position: absolute; left: 0; right: 0; bottom: 0; height: 46px; background: var(--ink);
  }
  .tagline-band .tagline {
    position: absolute; left: 26px; top: 50%; transform: translateY(-50%);
    color: var(--paper); font-size: 16px; font-weight: 400; white-space: nowrap;
  }
  .tagline-band .chevron { position: absolute; right: 76px; top: 0; }
</style>
</head>
<body>
<main class="sheet">
  <section class="card card-front" aria-label="Business card front">
    <div class="pattern-area" role="img" aria-label="Faint scattered paper and note shapes on black"></div>
    <div class="wordmark"><span class="mark-dot"></span><span class="mark-name">Brightwell<br>Consulting</span></div>
  </section>

  <section class="card card-back" aria-label="Business card back">
    <div class="wordmark"><span class="mark-dot"></span><span class="mark-name">Brightwell<br>Consulting</span></div>
    <div class="divider"></div>
    <div class="contact">
      <div class="name">Daniel Reyes</div>
      <div class="role">CEO</div>
      <div class="company">Brightwell Consulting consultancy<br>Riverton, OH.</div>
      <div class="line">
        <svg width="20" height="20" viewBox="0 0 20 20" aria-hidden="true"><rect width="20" height="20" rx="4" fill="#0b0b0b"/><path d="M6 5c1 0 1.5 2 1.5 2.5S6.5 8.5 6.7 9c.6 1.5 2.4 3.3 4 4 .5.2 1-1 1.5-1s2.5.5 2.5 1.5-1 2-2 2C8.5 15.5 4.5 11.5 4.5 7 4.5 6 5 5 6 5z" fill="#fff"/></svg>
        <span>404-555-0192</span>
      </div>
      <div class="line">
        <svg width="20" height="20" viewBox="0 0 20 20" aria-hidden="true"><rect width="20" height="20" rx="4" fill="#0b0b0b"/><rect x="4.5" y="6" width="11" height="8" fill="#fff"/><path d="M4.5 6l5.5 4.5L15.5 6" stroke="#0b0b0b" stroke-width="1.2" fill="none"/></svg>
        <span>daniel@brightwellconsulting.example</span>
      </div>
      <div class="line">
        <svg width="20" height="20" viewBox="0 0 20 20" aria-hidden="true"><rect width="20" height="20" rx="4" fill="#0b0b0b"/><circle cx="10" cy="10" r="5.5" fill="none" stroke="#fff" stroke-width="1.3"/><ellipse cx="10" cy="10" rx="2.3" ry="5.5" fill="none" stroke="#fff" stroke-width="1.1"/><path d="M4.5 10h11" stroke="#fff" stroke-width="1.1"/></svg>
        <span>www.brightwellconsulting.example</span>
      </div>
    </div>
    <div class="tagline-band">
      <span class="tagline">Momentum to Plan More, Lead More, Grow More</span>
      <svg class="chevron" width="30" height="46" viewBox="0 0 30 46" aria-hidden="true"><path d="M0 0h10l20 23-20 23H0l20-23z" fill="#fff"/></svg>
    </div>
  </section>
</main>
</body>
</html>
```